Settlewell88.com flyer for window coverings

two sided 8 1/2 x 11 flyer featuring window coverings to send people to our website to shop for window coverings. Can use stock photos of blinds and shutters (wood toned blinds, white shutters, grey roller shades, white faux wood blinds). We don't sell draperies or drapery rods. We do sell other product like lighting and cabinet organization but we would like this flyer to focus on window coverings. We want to be a resource for new home buyers that need items to finish making their new house their home.

Target Market(s)

New home buyers

Industry/Entity Type

Real Estate

Font styles to use
Sans Serif

Requirements
Must have
• photos of window blinds and shades--photos have been added 3/31
• logo of settlewell88.com
• "Settlewell88.com - #1 - Cover your windows for: Privacy, Security, Energy Efficiency. We have all the styles to meet your needs and installation available!"
Should not have
• Pictures of towel bars

```html
<!DOCTYPE html>
<html lang="en">
<head>
<meta charset="utf-8">
<title>Settlewell88.com – Window Coverings Flyer</title>
<link href="https://fonts.googleapis.com/css2?family=PT+Sans:wght@400;700&display=swap" rel="stylesheet">
<style>
  :root {
    --brand-red: #d0202b;
    --soft-grey: #cfcccb;
    --ink: #1e1e1e;
    --highlight: #ffec00;
    --white: #ffffff;
  }
  * { margin: 0; padding: 0; box-sizing: border-box; }
  html, body { width: 927px; height: 1200px; overflow: hidden; }
  body { font-family: "PT Sans", sans-serif; background: var(--white); }

  .flyer { position: relative; width: 927px; height: 1200px; overflow: hidden; }

  .backdrop {
    position: absolute; inset: 0;
    background:
      repeating-linear-gradient(178deg, rgba(255,255,255,0) 0 34px, rgba(205,205,205,0.35) 34px 52px),
      linear-gradient(90deg, #ececec 0%, #f7f7f7 45%, #e4e4e4 75%, #f2f2f2 100%);
  }

  .site-url {
    position: absolute; top: 14px; right: 22px;
    font-size: 20px; color: var(--brand-red); letter-spacing: 0.3px;
  }

  .brand {
    position: absolute; top: 88px; left: 68px;
    display: flex; align-items: center; gap: 14px;
  }
  .brand-dot { width: 44px; height: 44px; border-radius: 50%; background: var(--brand-red); }
  .brand-name { font-size: 44px; font-weight: 700; color: #3a3a3a; }

  .tagline {
    position: absolute; top: 190px; left: 40px; width: 590px;
    font-size: 19px; line-height: 25px; color: var(--ink);
  }
  .tagline strong { color: var(--brand-red); font-weight: 700; }

  .circles { position: absolute; inset: 0; }

  .offer-copy {
    position: absolute; left: 40px; width: 400px;
    color: var(--white); font-size: 24px; line-height: 31px; white-space: nowrap;
  }
  .offer-copy.intro { top: 494px; }
  .offer-copy.products { top: 741px; }
  .discount { color: var(--highlight); font-weight: 700; }

  .photo-column {
    position: absolute; left: 666px; top: 254px; width: 261px; height: 802px;
    background: var(--brand-red); padding: 3px;
    display: flex; flex-direction: column; gap: 4px;
  }
  .photo { flex: 1; }
  .photo.shutters { background: linear-gradient(135deg, #f4f4f2 0%, #d9dbd9 55%, #6b5e4c 100%); }
  .photo.arched-shutter { background: linear-gradient(180deg, #d8d2c8 0%, #ece8e0 50%, #5a4a3a 100%); }
  .photo.faux-wood { background: linear-gradient(160deg, #f3ecd2 0%, #e6dcc0 55%, #f7f3e6 100%); }

  .footer-line {
    position: absolute; left: 40px; top: 1159px;
    font-size: 21px; color: var(--ink); white-space: nowrap;
  }
  .footer-line strong { color: var(--brand-red); font-weight: 700; }
</style>
</head>
<body>
<main class="flyer">
  <div class="backdrop" role="img" aria-label="Soft blurred background of white window blinds"></div>

  <div class="site-url">www.settlewell88.com</div>

  <div class="brand">
    <span class="brand-dot"></span>
    <span class="brand-name">Settlewell88</span>
  </div>

  <p class="tagline"><strong>Settlewell88.com - #1 -</strong> Cover your windows for: Privacy, Security, Energy Efficiency. We have all the styles to meet your needs and installation available!</p>

  <svg class="circles" width="927" height="1200" viewBox="0 0 927 1200" aria-hidden="true">
    <circle cx="237" cy="689" r="379" fill="var(--soft-grey)" opacity="0.85"/>
    <circle cx="178" cy="687" r="333" fill="var(--brand-red)"/>
  </svg>

  <p class="offer-copy intro">Your builder and their supplier<br>have partner together to offer you<br>this special <span class="discount">10% discount</span> on a<br>wide variety of window blinds and<br>shades along with other products<br>to finish making your house your<br>home.</p>

  <p class="offer-copy products">We offer faux wood blinds, roller<br>shades, verticals, faux wood<br>shutters, sliding panels and honey<br>comb shades in a variety of colors<br>and finishes.</p>

  <div class="photo-column">
    <div class="photo shutters" role="img" aria-label="White plantation shutters on a window beside a table lamp"></div>
    <div class="photo arched-shutter" role="img" aria-label="White shutter in an arched window with candle holders on a console"></div>
    <div class="photo faux-wood" role="img" aria-label="White faux wood blinds on windows in a bright sitting room"></div>
  </div>

  <p class="footer-line">Visit us at: <strong>www.settlewell88.com.</strong>&nbsp; Live chat available to answer any questions you might have.</p>
</main>
</body>
</html>
```